Mosquito and outdoor pest management

The uploaded logo must be integrated as the main theme of the card. I would like it to be modern and eye catching. Maybe some backround images or light silver metallic background.
Space enough at the base for contact info to be put in- phone numbers,emails,names,website.
Space on the back for short blog and lines for hand writing..calling card.
Commercial- golf courses, schools, outdoor function properties, pre event treatments.
Residential- retirement villages, townhome complexes and general houses
Management

```html
<!DOCTYPE html>
<html lang="en">
<head>
<meta charset="utf-8">
<title>Brightyard Pest Services – Business Card</title>
<link href="https://fonts.googleapis.com/css2?family=Cinzel:wght@400;700&family=Lora:wght@400&display=swap" rel="stylesheet">
<style>
  :root {
    --backdrop: #2b2b2d;
    --card-front: #ffffff;
    --card-back: #c6c7c9;
    --ink: #141414;
    --accent: #e31b23;
    --divider: #6d6e70;
  }
  * { box-sizing: border-box; margin: 0; padding: 0; }
  html, body {
    width: 1200px; height: 900px; overflow: hidden;
    background: var(--backdrop);
  }
  .canvas { position: relative; width: 1200px; height: 900px; }

  .card {
    position: absolute;
    width: 560px; height: 320px;
    box-shadow: 0 10px 24px rgba(0,0,0,.45);
  }
  .card--front { left: 80px; top: 90px; background: var(--card-front); }
  .card--back  { left: 560px; top: 490px; background: var(--card-back); }

  .brand {
    position: absolute;
    display: flex; align-items: center; gap: 12px;
    font-family: "Lora", serif;
    font-weight: 400;
    font-size: 30px;
    color: var(--ink);
    line-height: 1.1;
    white-space: nowrap;
  }
  .brand__mark {
    width: 14px; height: 14px;
    background: var(--accent); flex: none;
  }

  .card--front .brand { left: 100px; top: 120px; }
  .card--back .brand  { left: 120px; top: 78px; }

  .holder {
    position: absolute; right: 248px; top: 205px;
    text-align: right;
  }
  .holder__name {
    font-family: "Cinzel", serif; font-weight: 700;
    font-size: 21px; color: var(--ink); letter-spacing: .5px;
    white-space: nowrap;
  }
  .holder__role {
    font-family: "Cinzel", serif; font-size: 12px;
    color: var(--accent); letter-spacing: 1px; margin-top: 2px;
  }
  .divider {
    position: absolute; left: 336px; top: 176px;
    width: 1px; height: 80px; background: var(--divider);
  }
  .contacts {
    position: absolute; left: 350px; top: 182px;
    list-style: none;
    font-family: "Lora", serif; font-size: 13px; color: var(--ink);
  }
  .contacts li { display: flex; align-items: center; gap: 7px; height: 23px; white-space: nowrap; }
  .contacts svg { width: 12px; height: 12px; flex: none; }
</style>
</head>
<body>
<div class="canvas">

  <section class="card card--front">
    <div class="brand">
      <span class="brand__mark"></span>
      <span class="brand__name">Brightyard Pest Services</span>
    </div>
  </section>

  <section class="card card--back">
    <div class="brand">
      <span class="brand__mark"></span>
      <span class="brand__name">Brightyard Pest Services</span>
    </div>

    <div class="holder">
      <p class="holder__name">LEON HARPER</p>
      <p class="holder__role">DIRECTOR</p>
    </div>

    <span class="divider"></span>

    <ul class="contacts">
      <li>
        <svg viewBox="0 0 24 24" aria-hidden="true"><path fill="#e31b23" d="M6.6 10.8a15 15 0 0 0 6.6 6.6l2.2-2.2c.3-.3.7-.4 1-.2 1.1.4 2.3.6 3.6.6.6 0 1 .4 1 1V20c0 .6-.4 1-1 1A17 17 0 0 1 3 4c0-.6.4-1 1-1h3.5c.6 0 1 .4 1 1 0 1.3.2 2.5.6 3.6.1.3 0 .7-.2 1z"/></svg>
        +330-5812-4470
      </li>
      <li>
        <svg viewBox="0 0 24 24" aria-hidden="true"><rect x="2.5" y="5" width="19" height="14" rx="1.5" fill="none" stroke="#e31b23" stroke-width="2"/><path d="M3 6l9 7 9-7" fill="none" stroke="#e31b23" stroke-width="2"/></svg>
        hello@leonharper.com
      </li>
      <li>
        <svg viewBox="0 0 24 24" aria-hidden="true"><circle cx="12" cy="12" r="9.5" fill="none" stroke="#e31b23" stroke-width="2"/><path d="M2.5 12h19M12 2.5c3 3 3 16 0 19M12 2.5c-3 3-3 16 0 19" fill="none" stroke="#e31b23" stroke-width="1.6"/></svg>
        www.brightyardpest.com
      </li>
    </ul>
  </section>

</div>
</body>
</html>
```